Sample site of what the customer is looking for:
www.dristanwheels.example - he doesn't like the girl in the background

- Looking for something easy to navigate, simple, yet different like Dristan Wheels

- For the background image, he's looking for a dusky night scene with a car or a road or something like that

- Accent color - match the logo which is attached unless a different color works better with the design

- Phone number: 555-014-7362

- The buttons for the menu will be: Home, Inventory, About Us & Contact Us

- No content on the homepage

```html
<!DOCTYPE html>
<html lang="en">
<head>
<meta charset="utf-8">
<title>Corvane Auto House</title>
<link rel="stylesheet" href="https://fonts.googleapis.com/css2?family=Encode+Sans+Semi+Condensed:wght@400;600&display=swap">
<style>
  :root {
    --ink-white: #ffffff;
    --accent-gold: #e0b22a;
    --night-deep: #1c1b1c;
    --night-mid: #3a3737;
    --night-haze: #5a5655;
    --brick-warm: #4a2f2c;
    --rule-faint: rgba(255, 255, 255, 0.14);
    --body-font: "Encode Sans Semi Condensed", "Arial Narrow", sans-serif;
  }
  * { margin: 0; padding: 0; box-sizing: border-box; }
  html, body {
    width: 1200px;
    height: 788px;
    overflow: hidden;
    background: var(--night-deep);
  }
  .site {
    position: relative;
    width: 1200px;
    height: 788px;
    overflow: hidden;
    font-family: var(--body-font);
    color: var(--ink-white);
  }
  .hero-backdrop {
    position: absolute;
    inset: 0;
    background:
      radial-gradient(ellipse 520px 380px at 860px 330px, rgba(120, 116, 112, 0.45), transparent 70%),
      radial-gradient(ellipse 300px 500px at 1170px 400px, rgba(92, 52, 50, 0.55), transparent 70%),
      radial-gradient(ellipse 420px 520px at 80px 420px, rgba(78, 46, 40, 0.45), transparent 70%),
      linear-gradient(180deg, var(--night-mid) 0%, var(--night-haze) 32%, var(--night-mid) 62%, var(--night-deep) 100%);
  }
  .hero-backdrop::after {
    content: "";
    position: absolute;
    inset: 0;
    background: radial-gradient(ellipse at 50% 45%, transparent 40%, rgba(0, 0, 0, 0.55) 100%);
  }
  .brand {
    position: absolute;
    top: 58px;
    right: 68px;
    width: 200px;
    text-align: center;
    font-size: 35px;
    font-weight: 400;
    line-height: 1.15;
    color: var(--ink-white);
  }
  .main-nav {
    position: absolute;
    top: 244px;
    left: 988px;
    width: 90px;
    list-style: none;
  }
  .main-nav li {
    height: 47px;
    line-height: 42px;
    text-align: center;
    font-size: 16px;
    border-bottom: 1px solid var(--rule-faint);
  }
  .main-nav a { color: var(--ink-white); text-decoration: none; }
  .headline {
    position: absolute;
    top: 232px;
    left: 131px;
    font-size: 58px;
    font-weight: 600;
    line-height: 76px;
    letter-spacing: 0.2px;
    text-transform: uppercase;
  }
  .headline .accent { color: var(--accent-gold); display: block; }
  .headline span { display: block; }
  .site-footer {
    position: absolute;
    top: 734px;
    left: 0;
    width: 1200px;
    height: 26px;
    font-size: 15.5px;
    line-height: 26px;
  }
  .footer-contact { position: absolute; left: 352px; white-space: nowrap; }
  .footer-contact .divider { margin: 0 14px; }
  .footer-credit { position: absolute; left: 766px; white-space: nowrap; }
  .social-links {
    position: absolute;
    left: 1000px;
    top: 2px;
    display: flex;
    gap: 7px;
  }
  .social-links svg { display: block; }
</style>
</head>
<body>
<div class="site">
  <div class="hero-backdrop" role="img" aria-label="Dusky night scene of a cobbled street between brick warehouses, with city towers in the distance"></div>

  <div class="brand">Corvane<br>Auto House</div>

  <ul class="main-nav">
    <li><a href="#">Home</a></li>
    <li><a href="#">Inventory</a></li>
    <li><a href="#">About Us</a></li>
    <li><a href="#">Contact Us</a></li>
  </ul>

  <h1 class="headline">
    <span>Nam quis arcu sit</span>
    <span class="accent">Amet est</span>
    <span>Dictum volutpat</span>
  </h1>

  <footer class="site-footer">
    <div class="footer-contact">482, Marlow Lane. Fenwick, Texas<span class="divider">|</span>555-014-7362</div>
    <div class="footer-credit">Powered by Cardex Works</div>
    <div class="social-links" aria-label="Social links">
      <svg width="22" height="22" viewBox="0 0 22 22"><circle cx="11" cy="11" r="11" fill="#ffffff"/></svg>
      <svg width="22" height="22" viewBox="0 0 22 22"><circle cx="11" cy="11" r="11" fill="#ffffff"/></svg>
      <svg width="22" height="22" viewBox="0 0 22 22"><circle cx="11" cy="11" r="11" fill="#ffffff"/></svg>
      <svg width="22" height="22" viewBox="0 0 22 22"><circle cx="11" cy="11" r="11" fill="#ffffff"/></svg>
    </div>
  </footer>
</div>
</body>
</html>
```